Kestrel Bridge Consulting (KBC) Business Card Design

I would like to create double-sided business cards that contain:
1) Name: Derek Molvane
2) Phone Number: +1 (555) 218-4907
3) Email: Derek.Molvane@KestrelBridgeConsulting.example
4) Website: KestrelBridgeConsulting.example

I would like to include my logo and a color scheme similar to the Varnholt Grand Prix Ostera squad color scheme (black, silver, greenish-blue – but can also include regular blue)

What we do: Our company develops and delivers innovative and pragmatic information technology and cybersecurity risk and compliance solutions for organizations in the commercial market as well as the federal, and state/local sectors.

```html
<!DOCTYPE html>
<html lang="en">
<head>
<meta charset="utf-8">
<title>Kestrel Bridge Consulting — Business Card</title>
<link rel="stylesheet" href="https://fonts.googleapis.com/css2?family=Montserrat:wght@400;700&family=Roboto:wght@400&display=swap">
<style>
  :root {
    --canvas: #e9e9e9;
    --ink: #111111;
    --card-black: #141414;
    --card-black-light: #2c2c2c;
    --card-white: #ffffff;
    --teal: #21b3a8;
    --blue: #1f5fa8;
    --faint: #eef2f5;
    --text-dark: #1a1a1a;
    --text-body: #333333;
    --white: #ffffff;
  }
  * { box-sizing: border-box; margin: 0; padding: 0; }
  html, body { width: 1200px; height: 1200px; overflow: hidden; }
  body {
    background: var(--canvas);
    font-family: "Montserrat", Arial, sans-serif;
    display: flex;
    flex-direction: column;
    align-items: center;
    justify-content: center;
    gap: 64px;
  }
  .card {
    position: relative;
    width: 880px;
    height: 500px;
    overflow: hidden;
    box-shadow: 0 6px 18px rgba(0,0,0,0.12);
  }

  /* Front */
  .card-front { background: var(--card-black); }
  .front-texture {
    position: absolute; inset: 0;
    background:
      linear-gradient(135deg, var(--card-black-light) 0%, var(--card-black) 45%, #1e1e1e 70%, var(--card-black) 100%);
  }
  .front-lockup {
    position: absolute;
    left: 170px; top: 190px;
    display: flex; align-items: center; gap: 34px;
  }
  .brand-dot {
    width: 104px; height: 104px;
    border-radius: 50%;
    background: var(--teal);
    flex: none;
  }
  .brand-name {
    font-family: "Montserrat", Arial, sans-serif;
    font-weight: 400;
    text-transform: uppercase;
    letter-spacing: 1px;
    line-height: 1.02;
  }
  .front-lockup .brand-name { color: var(--white); font-size: 38px; }

  /* Back */
  .card-back { background: var(--card-white); }
  .back-watermark {
    position: absolute;
    left: 560px; top: 140px;
    width: 360px; height: 360px;
    border-radius: 50%;
    background: var(--faint);
  }
  .back-lockup {
    position: absolute;
    right: 46px; top: 58px;
    display: flex; align-items: center; gap: 16px;
  }
  .back-lockup .brand-dot { width: 64px; height: 64px; }
  .back-lockup .brand-name { color: var(--text-dark); font-size: 22px; }

  .holder {
    position: absolute;
    left: 44px; top: 262px;
  }
  .holder-name {
    font-family: "Montserrat", Arial, sans-serif;
    font-weight: 700;
    font-size: 30px;
    letter-spacing: 0.5px;
    color: var(--text-dark);
    text-transform: uppercase;
    margin-bottom: 26px;
  }
  .contact-list { list-style: none; }
  .contact-item {
    display: flex; align-items: center; gap: 12px;
    font-family: "Roboto", Arial, sans-serif;
    font-size: 22px;
    color: var(--text-body);
    line-height: 35px;
  }
  .contact-icon { width: 18px; height: 18px; flex: none; fill: var(--text-body); }

  .back-footer { position: absolute; left: 0; bottom: 0; width: 880px; height: 60px; }
</style>
</head>
<body>

  <section class="card card-front" aria-label="Business card front">
    <div class="front-texture" role="img" aria-label="Dark faceted low-poly background texture"></div>
    <div class="front-lockup">
      <span class="brand-dot"></span>
      <div class="brand-name">Kestrel<br>Bridge<br>Consulting</div>
    </div>
  </section>

  <section class="card card-back" aria-label="Business card back">
    <div class="back-watermark"></div>
    <div class="back-lockup">
      <span class="brand-dot"></span>
      <div class="brand-name">Kestrel<br>Bridge<br>Consulting</div>
    </div>

    <div class="holder">
      <h1 class="holder-name">Derek Molvane</h1>
      <ul class="contact-list">
        <li class="contact-item">
          <svg class="contact-icon" viewBox="0 0 24 24" aria-hidden="true"><path d="M6.6 10.8a15.1 15.1 0 0 0 6.6 6.6l2.2-2.2a1 1 0 0 1 1-.25 11.4 11.4 0 0 0 3.6.57 1 1 0 0 1 1 1V20a1 1 0 0 1-1 1A17 17 0 0 1 3 4a1 1 0 0 1 1-1h3.5a1 1 0 0 1 1 1c0 1.25.2 2.45.57 3.57a1 1 0 0 1-.25 1z"/></svg>
          +1 (555) 218-4907
        </li>
        <li class="contact-item">
          <svg class="contact-icon" viewBox="0 0 24 24" aria-hidden="true"><path d="M2 5h20v14H2z M3.5 6.5 12 13l8.5-6.5" fill="none" stroke="#333" stroke-width="0"/><path d="M2 5h20v14H2zm2 2v.4l8 5.6 8-5.6V7z"/></svg>
          Derek.Molvane@KestrelBridgeConsulting.example
        </li>
        <li class="contact-item">
          <svg class="contact-icon" viewBox="0 0 24 24" aria-hidden="true"><circle cx="12" cy="12" r="9.5" fill="none" stroke="#333" stroke-width="2"/><ellipse cx="12" cy="12" rx="4" ry="9.5" fill="none" stroke="#333" stroke-width="2"/><path d="M2.5 12h19" stroke="#333" stroke-width="2"/></svg>
          KestrelBridgeConsulting.example
        </li>
      </ul>
    </div>

    <svg class="back-footer" viewBox="0 0 880 60" preserveAspectRatio="none" aria-hidden="true">
      <polygon points="0,22 490,22 520,60 0,60" fill="var(--ink)"/>
      <polygon points="490,22 880,22 880,60 520,60" fill="var(--ink)"/>
      <polygon points="480,0 880,0 880,38 512,38" fill="var(--teal)"/>
    </svg>
  </section>

</body>
</html>
```